Security Warning Sign

We have an existing sign that needs an update. I have attached a picture of the current square sign. We need to maintain the same wording. It needs to be professional and appropriate to attach to our customers fence. Also attached is a copy of our building sign which may lend some inspiration and hopefully the ai format will assist. The final sign will be 600mm x 600mmOur website is www.harbourlinewatch.com.au

```html
<!DOCTYPE html>
<html lang="en">
<head>
<meta charset="utf-8">
<title>Warning – Electronic Surveillance Sign</title>
<link rel="stylesheet" href="https://fonts.googleapis.com/css2?family=Roboto+Condensed:wght@700;800;900&family=Open+Sans:wght@800&display=swap">
<style>
  :root {
    --orange: #f58522;
    --white: #ffffff;
    --charcoal: #272727;
    --yellow: #fde018;
    --outline: #3a2a20;
    --stripe-grey: #4a4a4a;
  }
  html, body {
    margin: 0;
    padding: 0;
    width: 1200px;
    height: 1200px;
    overflow: hidden;
    background: var(--orange);
  }
  .sign {
    display: block;
    width: 1200px;
    height: 1200px;
  }
  .headline {
    font-family: "Roboto Condensed", "Arial Narrow", sans-serif;
    font-weight: 800;
    fill: var(--orange);
  }
  .notice {
    font-family: "Roboto Condensed", "Arial Narrow", sans-serif;
    font-weight: 900;
    fill: var(--white);
  }
  .area-note {
    font-family: "Roboto Condensed", "Arial Narrow", sans-serif;
    font-weight: 800;
    fill: var(--orange);
    stroke: var(--outline);
    stroke-width: 2;
    paint-order: stroke;
  }
  .company-name {
    font-family: "Open Sans", Arial, sans-serif;
    font-weight: 800;
    fill: var(--white);
  }
  .contact {
    font-family: "Open Sans", Arial, sans-serif;
    font-weight: 800;
    fill: var(--white);
  }
</style>
</head>
<body>
<svg class="sign" viewBox="0 0 1200 1200" xmlns="http://www.w3.org/2000/svg">
  <!-- background -->
  <rect class="field" x="0" y="0" width="1200" height="1200" fill="var(--orange)"/>

  <!-- white frame -->
  <rect class="frame" x="34" y="98" width="1143" height="714" fill="var(--white)"/>

  <!-- dark warning panel with header tab -->
  <rect class="panel" x="62" y="126" width="1087" height="658" fill="var(--charcoal)"/>
  <rect class="header-tab" x="174" y="20" width="863" height="194" fill="var(--white)"/>

  <!-- headline -->
  <text class="headline" x="248" y="189" font-size="212" textLength="703" lengthAdjust="spacingAndGlyphs">WARNING</text>

  <!-- camera illustrations -->
  <rect class="camera camera-left" role="img" aria-label="Orange CCTV camera on wall bracket, facing right" x="66" y="218" width="196" height="114" rx="12" fill="var(--orange)"/>
  <rect class="camera camera-right" role="img" aria-label="Orange CCTV camera on wall bracket, facing left" x="962" y="222" width="181" height="118" rx="12" fill="var(--orange)"/>

  <!-- notice text -->
  <text class="notice" x="117" y="424" textLength="414" lengthAdjust="spacingAndGlyphs"><tspan font-size="114">E</tspan><tspan font-size="82">LECTRONIC</tspan></text>
  <text class="notice" x="115" y="537" font-size="82" textLength="479" lengthAdjust="spacingAndGlyphs">SURVEILLANCE</text>
  <text class="notice" x="114" y="651" font-size="82" textLength="532" lengthAdjust="spacingAndGlyphs">AND  RECORDING</text>
  <text class="notice" x="116" y="764" font-size="82" textLength="268" lengthAdjust="spacingAndGlyphs">DEVICES</text>

  <!-- yellow triangle -->
  <polygon class="triangle" points="587,349 1113,349 850,750" fill="var(--yellow)"/>
  <text class="area-note" x="664" y="446" font-size="108" textLength="377" lengthAdjust="spacingAndGlyphs">INSTALLED</text>
  <text class="area-note" x="738" y="564" font-size="108" textLength="229" lengthAdjust="spacingAndGlyphs">IN THE</text>
  <text class="area-note" x="770" y="681" font-size="108" textLength="184" lengthAdjust="spacingAndGlyphs">AREA</text>

  <!-- company band -->
  <rect class="company-band" x="0" y="813" width="1200" height="387" fill="var(--charcoal)"/>
  <circle class="company-mark" cx="358" cy="972" r="95" fill="var(--orange)"/>
  <text class="company-name" x="520" y="932" font-size="70" textLength="455" lengthAdjust="spacingAndGlyphs">HARBOURLINE</text>
  <text class="company-name" x="520" y="1002" font-size="70" textLength="268" lengthAdjust="spacingAndGlyphs">WATCH</text>
  <text class="company-name" x="520" y="1071" font-size="70" textLength="333" lengthAdjust="spacingAndGlyphs">SERVICES</text>

  <!-- contact strip -->
  <polygon class="stripe-grey" points="733,1127 742,1127 699,1200 689,1200" fill="var(--stripe-grey)"/>
  <polygon class="stripe-orange" points="764,1107 777,1107 733,1200 711,1200" fill="var(--orange)"/>
  <polygon class="phone-tab" points="786,1107 1200,1107 1200,1200 731,1200" fill="var(--orange)"/>

  <text class="contact website" x="47" y="1164" font-size="33" textLength="645" lengthAdjust="spacingAndGlyphs">WWW.HARBOURLINEWATCH.COM.AU</text>

  <g class="phone-icon" fill="none" stroke="var(--white)" stroke-width="4" stroke-linecap="round">
    <path d="M827 1133 c6 5 6 12 2 19 c-8 12 -18 21 -30 25 c-5 2 -10 0 -12 -4 l4 -3 c3 2 6 2 9 1 c9 -4 17 -12 22 -22 c1 -3 0 -6 -2 -9 z" fill="var(--white)" stroke="none"/>
    <path d="M791 1151 a18 18 0 0 1 18 -18"/>
    <path d="M798 1152 a11 11 0 0 1 11 -11"/>
    <circle cx="806" cy="1150" r="2" fill="var(--white)" stroke="none"/>
  </g>
  <text class="contact phone" x="846" y="1171" font-size="51" textLength="303" lengthAdjust="spacingAndGlyphs">1300 555 014</text>
</svg>
</body>
</html>
```